Business IT Services Billboard to attract local small businesses

We are Brivolane, a premier Managed Service Provider (MSP) specializing in comprehensive IT services and VOIP phone solutions exclusively for businesses. Our goal is to create a dynamic and visually engaging billboard advertisement that not only highlights our cutting-edge IT solutions but also emphasizes our state-of-the-art VOIP phone services. This billboard should communicate our commitment to providing innovative, reliable, and holistic technology solutions.
Target Market(s)
small business
Industry/Entity Type
Information Technology
Colors
Designer to choose colors to be used in the design.
Look and feel
Each slider illustrates characteristics of the customer's brand and the style your logo design should communicate.

```html
<!DOCTYPE html>
<html lang="en">
<head>
<meta charset="utf-8">
<title>Brivolane Billboard</title>
<link rel="stylesheet" href="https://fonts.googleapis.com/css2?family=Montserrat:wght@400;500;700;800&display=swap">
<style>
  :root {
    --page: #ffffff;
    --brand-blue: #1b63a6;
    --ink: #0d1626;
    --band-grey: #a7a7a7;
    --rule-grey: #b9b9b9;
    --photo-light: #eef0f3;
    --photo-mid: #c9d0da;
    --photo-navy: #26324a;
  }
  * { box-sizing: border-box; margin: 0; padding: 0; }
  html, body {
    width: 888px;
    height: 1200px;
    overflow: hidden;
    background: var(--page);
    font-family: "Montserrat", sans-serif;
  }
  .billboard {
    position: absolute;
    left: 44px;
    top: 403px;
    width: 800px;
    height: 394px;
    background: var(--page);
    box-shadow: 0 10px 40px rgba(0, 0, 0, 0.22);
    overflow: hidden;
  }
  .brand-name {
    position: absolute;
    left: 28px;
    top: 20px;
    font-weight: 800;
    font-size: 34px;
    letter-spacing: 1px;
    color: var(--brand-blue);
    text-transform: uppercase;
  }
  .headline-band {
    position: absolute;
    left: 18px;
    top: 69px;
    width: 771px;
    height: 130px;
    background: var(--brand-blue);
  }
  .hero-photo {
    position: absolute;
    left: 300px;
    top: 22px;
    width: 470px;
    height: 318px;
    background:
      radial-gradient(ellipse 32% 60% at 68% 55%, var(--photo-navy) 0%, rgba(38, 50, 74, 0.6) 55%, rgba(38, 50, 74, 0) 100%),
      radial-gradient(ellipse 30% 28% at 38% 72%, #2a2a2a 0%, rgba(42, 42, 42, 0) 100%),
      linear-gradient(90deg, rgba(238, 240, 243, 0) 0%, var(--photo-light) 25%, var(--photo-mid) 100%);
    opacity: 0.95;
  }
  .headline {
    position: absolute;
    left: 29px;
    top: 78px;
    font-weight: 800;
    font-size: 28px;
    line-height: 37px;
    color: #ffffff;
    text-transform: uppercase;
    letter-spacing: -0.3px;
  }
  .headline .accent {
    display: block;
    color: var(--ink);
    font-size: 31px;
  }
  .tagline {
    position: absolute;
    left: 29px;
    top: 226px;
    width: 270px;
    font-weight: 400;
    font-size: 17px;
    line-height: 25px;
    color: var(--ink);
  }
  .cta-strip {
    position: absolute;
    left: 0;
    top: 340px;
    width: 800px;
    height: 36px;
  }
  .cta-text {
    position: absolute;
    left: 29px;
    top: 346px;
    font-weight: 700;
    font-size: 19px;
    color: var(--ink);
  }
  .web-address {
    position: absolute;
    left: 406px;
    top: 346px;
    font-weight: 700;
    font-size: 19px;
    letter-spacing: 4.6px;
    color: var(--brand-blue);
  }
</style>
</head>
<body>
  <div class="billboard">
    <div class="headline-band"></div>
    <div class="hero-photo" role="img" aria-label="Photo of an excited businessman wearing a headset, raising both hands in front of a laptop on a white office desk"></div>
    <div class="brand-name">Brivolane</div>
    <h1 class="headline">
      Elevate your business<br>
      with next-gen IT and
      <span class="accent">VOIP services</span>
    </h1>
    <p class="tagline">Innovative&nbsp; IT and VOIP Solu­tions Tailored for Your Busi­ness Success.</p>
    <svg class="cta-strip" viewBox="0 0 800 36" width="800" height="36" aria-hidden="true">
      <polygon points="0,0 470,0 483,35 0,35" fill="var(--band-grey)"/>
      <line x1="483" y1="35" x2="800" y2="35" stroke="var(--rule-grey)" stroke-width="1.5"/>
    </svg>
    <p class="cta-text">Transform Your Tech Today at</p>
    <p class="web-address">www.brivolane.com</p>
  </div>
</body>
</html>
```